Halvering Cove Books -- young adult, fantasy for small publisher looking for long term relationship fo

THE PALE HARBOR.
YA fantasy. Torvin, black hair, grey eyes, lives alone in a decaying red metropolis. Alone that is except for the body drifting slowly to shore and the shadows who look after him, tutor him, etc. He will have to fight against a non-human army if he is to win his way off the island and THE PALE HARBOR.
AUTHOR -- DEREK J. FOLSTON
SERIES -- CHRONICLE OF THE GLIMMERING STRAIT
book size -- 5 x 8

Target Market(s)

Age 12+ boys, adults who read fantasy

Industry/Entity Type

Book Publisher

Requirements
Must have
• red city in background, boy's face -- black hair, grey eyes, sea (if possible). I need something that will POP on North American bookshelves, something that will scream out BUY ME BUY ME!!!

```html
<!DOCTYPE html>
<html lang="en">
<head>
<meta charset="UTF-8">
<title>The Pale Harbor — Book Cover</title>
<link rel="stylesheet" href="https://fonts.googleapis.com/css2?family=Bebas+Neue&family=Montserrat:wght@600;700&family=Open+Sans:wght@400&display=swap">
<style>
  :root {
    --stage: #ececec;
    --cover-red: #e0171c;
    --cover-red-deep: #c81217;
    --image-light: #ff9a8a;
    --image-mid: #e8453d;
    --image-dark: #8e0d12;
    --title-ink: #ececec;
    --body-ink: #f6d6d6;
    --panel-dark: #6b0a0e;
  }
  * { box-sizing: border-box; margin: 0; padding: 0; }
  html, body {
    width: 1200px; height: 800px; overflow: hidden;
    background: var(--stage);
  }
  .stage {
    position: relative; width: 1200px; height: 800px;
    display: flex; justify-content: center; align-items: center; gap: 80px;
  }
  .cover {
    position: relative; width: 400px; height: 640px;
    background: var(--cover-red); overflow: hidden;
    box-shadow: 0 18px 40px rgba(0,0,0,0.18);
  }

  /* Back cover */
  .back-cover { background: var(--cover-red-deep); padding: 34px 30px 0; }
  .back-author {
    font-family: "Montserrat", sans-serif; font-weight: 700; font-size: 13px;
    color: var(--title-ink); text-align: right; letter-spacing: 0.5px;
  }
  .back-title {
    font-family: "Bebas Neue", sans-serif; font-size: 60px; line-height: 1;
    color: var(--title-ink); text-align: center; margin-top: 10px;
  }
  .back-series {
    font-family: "Montserrat", sans-serif; font-weight: 600; font-size: 10px;
    letter-spacing: 2px; color: var(--title-ink); text-align: center; margin-top: 8px;
  }
  .back-blurb {
    font-family: "Open Sans", sans-serif; font-size: 11.5px; line-height: 15.5px;
    color: var(--body-ink); text-align: justify; margin-top: 24px;
    height: 328px; overflow: hidden;
  }
  .back-blurb p + p { margin-top: 8px; }
  .back-panels {
    position: absolute; left: 30px; right: 30px; bottom: 26px;
    display: flex; justify-content: space-between; align-items: flex-end;
  }
  .panel {
    width: 92px; height: 62px; background: var(--panel-dark);
    display: flex; align-items: center; justify-content: center;
    font-family: "Open Sans", sans-serif; font-size: 10px; color: var(--body-ink);
  }

  /* Front cover */
  .cover-art {
    position: absolute; left: 0; top: 0; width: 400px; height: 320px;
    background:
      linear-gradient(180deg, rgba(224,23,28,0) 60%, var(--cover-red) 100%),
      radial-gradient(ellipse at 50% 15%, var(--image-light) 0%, var(--image-mid) 45%, var(--image-dark) 100%);
  }
  .front-text {
    position: absolute; left: 0; right: 0; top: 318px;
    text-align: center; color: var(--title-ink);
  }
  .front-title-small {
    font-family: "Bebas Neue", sans-serif; font-size: 80px; line-height: 0.9;
  }
  .front-title-large {
    font-family: "Bebas Neue", sans-serif; font-size: 88px; line-height: 0.95;
    letter-spacing: -0.5px;
  }
  .front-series {
    font-family: "Montserrat", sans-serif; font-weight: 600; font-size: 11px;
    letter-spacing: 2px; margin-top: 18px;
  }
  .front-author {
    font-family: "Montserrat", sans-serif; font-weight: 700; font-size: 15px;
    letter-spacing: 0.5px; margin-top: 26px;
  }
</style>
</head>
<body>
<main class="stage">
  <section class="cover back-cover">
    <p class="back-author">DEREK J. FOLSTON</p>
    <h2 class="back-title">THE PALE HARBOR</h2>
    <p class="back-series">CHRONICLE OF THE GLIMMERING STRAIT</p>
    <div class="back-blurb">
      <p>Torvin has grown up alone among the crumbling towers of a red city that forgot its own name. Only the shadows keep him company, teaching him letters, blades and the old tongue of the tides. Then a body drifts toward the shore, and with it comes word of an army that is not human. To survive, Torvin must learn what the shadows have hidden, face the host gathering beyond the walls, and find a way across the glimmering strait before the harbor turns pale forever. A sweeping first chapter of a saga about courage, loss and the long road home.</p>
      <p>Derek J. Folston brings a dark and luminous world to life, where every street hides a secret and every tide carries a warning. Readers who crave danger, loyalty and wonder will find all three waiting in the ruins. The shadows are watching. The sea is rising. And Torvin is running out of time to choose who he will become when the last light fades over the water.</p>
    </div>
    <div class="back-panels">
      <div class="panel">LOGO</div>
      <div class="panel">ISBN</div>
    </div>
  </section>

  <section class="cover front-cover">
    <div class="cover-art" role="img" aria-label="Red-toned city skyline at night above the sea, with light rays fanning out behind the towers"></div>
    <div class="front-text">
      <h1>
        <span class="front-title-small" style="display:block">THE</span>
        <span class="front-title-large" style="display:block">PALE HARBOR</span>
      </h1>
      <p class="front-series">CHRONICLE OF THE GLIMMERING STRAIT</p>
      <p class="front-author">DEREK J. FOLSTON</p>
    </div>
  </section>
</main>
</body>
</html>
```